BrightWanderDoc.com Blog Design (Travel, Lifestyle, and Life Hacking blog)

I am launching a lifestyle blog about my life. I'm a doctor who travels the world trying the best restaurants, airlines and trying to have as much fun as possible. I also invest in startups, and am always trying new tricks to make life better. I also plan to write about various other topics, but essentially it is about travel, lifestyle and medicine. I need a creative and really awesome looking design for a new wordpress blog called BrightWanderDoc

Target Market(s)

Physicians, Entrepreneurs, Travellers

Industry/Entity Type

Airlines

Number of Pages Required

1 page

Font styles to use
Serif

Requirements
Must have
• Slick looking graphics with a highly professional modern feel

```html
<!DOCTYPE html>
<html lang="en">
<head>
<meta charset="utf-8">
<title>BrightWanderDoc – Travel, Lifestyle &amp; Medicine</title>
<link href="https://fonts.googleapis.com/css2?family=Montserrat:wght@400;500;600;700&display=swap" rel="stylesheet">
<style>
:root{
  --ink:#1b1b1b;
  --muted:#6f6f6f;
  --paper:#ffffff;
  --night:#050505;
  --tag:#f3e500;
  --line:#d9d9d9;
  --friend:#3c5a99;
  --chirp:#2aaee2;
  --link:#1f78b4;
  --view:#e04a3a;
}
*{margin:0;padding:0;box-sizing:border-box}
html,body{width:1200px;height:4500px;overflow:hidden}
body{font-family:"Montserrat",Arial,sans-serif;color:var(--ink);background:var(--paper);position:relative}
section,header,footer{position:absolute;left:0;width:1200px}
.abs{position:absolute}
.ph{position:absolute;display:block}

/* image tones */
.t-canyon{background:linear-gradient(160deg,#6b3a1f,#2b150b 70%,#1a0c07)}
.t-ruins{background:linear-gradient(180deg,#8fb3d6,#c99a5c 55%,#6f4a28)}
.t-dock{background:linear-gradient(180deg,#d9d3c2,#9c8f78 50%,#3a3027)}
.t-beach{background:linear-gradient(180deg,#3b8fd1,#8fc8e6 45%,#2f8a4a 70%,#e8dcc0)}
.t-lagoon{background:linear-gradient(180deg,#7fb4e0,#4c6b4a 45%,#1f7f6e 80%,#2a4a3a)}
.t-spiral{background:radial-gradient(circle at 50% 55%,#3c4a4c,#1c2628 70%)}
.t-city{background:linear-gradient(180deg,#0d2f7a,#1f5cc2 45%,#e2a03c 70%,#0b1c3a)}
.t-temple{background:linear-gradient(180deg,#a7c4de,#c4a060 60%,#7a5a30)}
.t-warm{background:linear-gradient(180deg,#caa27a,#8a5a3c 60%,#4a2e1e)}
.t-road{background:linear-gradient(180deg,#3f7fd6,#8cb6e6 45%,#4a4a4a 70%,#b04030)}
.t-mount{background:linear-gradient(180deg,#c9c9c9,#7d7d7d 60%,#3b3b3b)}
.t-peaks{background:linear-gradient(180deg,#6a9ad2,#5d6a7a 50%,#7a8a4a)}
.t-desert{background:linear-gradient(180deg,#dcd6c8,#b7a58a 55%,#7c6a52)}
.t-skyline{background:linear-gradient(180deg,#7aa6d6,#c8b48a 60%,#8a7a5a)}
.t-ship{background:linear-gradient(180deg,#4b86cf,#c8d8ea 60%,#2a4a6a)}
.t-tower{background:linear-gradient(180deg,#f0a04a,#6a8ac0 50%,#4a3a2a)}
.t-pagoda{background:linear-gradient(180deg,#f6d68a,#c87a2a 55%,#3a2a1a)}
.t-tiger{background:linear-gradient(160deg,#e8e4dc,#9a9080 60%,#2a2620)}
.t-wall{background:linear-gradient(180deg,#9ac0e0,#4e7a4a 55%,#2e4a2a)}
.t-palm{background:linear-gradient(180deg,#2f7a3a,#63b3d8 40%,#2aa7c0 65%,#efe2c4)}
.t-canal{background:linear-gradient(180deg,#7fb6e6,#b86a4a 55%,#3a5a6a)}
.t-palace{background:linear-gradient(180deg,#f2c97a,#d9b88a 55%,#6a5a3a)}
.t-rock{background:linear-gradient(90deg,#8a4a22,#c0703a 40%,#7a3a1a 70%,#b86a34)}

/* common bits */
.tag{display:inline-block;background:var(--tag);color:#111;font-size:8px;font-weight:700;letter-spacing:.5px;padding:2px 5px;text-transform:uppercase}
.meta{font-size:9px;color:var(--muted);display:flex;gap:16px;align-items:center;white-space:nowrap}
.meta span{display:inline-flex;align-items:center;gap:6px}
.meta .c::before{content:"";width:9px;height:7px;background:currentColor;border-radius:2px;display:inline-block}
.meta .d::before{content:"";width:8px;height:8px;border:1.5px solid currentColor;display:inline-block}
.on-dark .meta{color:#cfcfcf}

/* header */
.site-header{top:0;height:504px}
.site-header .backdrop{left:0;top:0;width:1200px;height:504px}
.logo{left:0;width:1200px;top:48px;text-align:center;color:#fff;font-size:28px;font-weight:700;letter-spacing:-.3px}
.top-icons{right:120px;top:10px;display:flex;gap:14px}
.top-icons i{width:9px;height:9px;background:#d8d8d8;border-radius:50%;display:block}
.tools{right:150px;top:50px;display:flex;gap:44px}
.nav{left:0;width:1200px;top:102px;display:flex;justify-content:center;gap:34px;color:#fff;font-size:12px;font-weight:600}
.hero-card{top:150px;width:282px;height:300px;overflow:hidden}
.hero-card .ph{inset:0}
.hero-card .cap{position:absolute;left:18px;right:14px;bottom:28px;color:#fff}
.hero-card h3{font-size:15px;font-weight:700;line-height:20px;margin:6px 0 8px}

/* minis: thumb on the left, title then meta stacked on the right */
.mini{position:absolute;width:270px;min-height:66px;display:grid;grid-template-columns:66px 1fr;grid-template-rows:auto 1fr;column-gap:16px}
.mini .ph{position:relative;grid-row:1 / 3;grid-column:1;width:66px;height:66px}
.mini h4{grid-column:2;grid-row:1;font-size:11px;line-height:15px;font-weight:700;letter-spacing:-.1px}
.mini .meta{grid-column:2;grid-row:2;align-self:start;margin-top:7px}
.side .mini{width:255px}

/* feature cards */
.card{position:absolute;overflow:hidden;color:#fff}
.card .ph{inset:0}
.card .cap{position:absolute;left:16px;right:12px;bottom:18px}
.card h3{font-size:15px;font-weight:700;line-height:20px;margin:6px 0 6px}

.dots{position:absolute;left:414px;display:flex;gap:10px}
.dots i{width:8px;height:8px;border-radius:50%;background:#222;display:block}
.dots i.on{background:var(--tag)}

.social{position:absolute;left:783px;width:255px;height:48px;color:#fff;font-size:12px;font-weight:600;display:flex;align-items:center;padding-left:54px}
.social::before{content:"";position:absolute;left:0;top:0;width:42px;height:48px;background:rgba(0,0,0,.15)}
.social::after{content:"";position:absolute;left:16px;top:19px;width:10px;height:10px;background:#fff;border-radius:2px}
.s-friend{background:var(--friend)}.s-chirp{background:var(--chirp)}.s-link{background:var(--link)}.s-view{background:var(--view)}

/* feed */
.lead h2{font-size:19px;font-weight:700;line-height:26px}
.excerpt{font-size:10px;line-height:16px;color:var(--muted)}
.post-row{position:absolute;left:165px;width:570px;height:132px}
.post-row .ph{left:0;top:0;width:189px;height:132px}
.post-row .body{position:absolute;left:210px;top:0;width:360px}
.post-row h4{font-size:12px;font-weight:700;line-height:17px;margin:6px 0 6px}
.pager{position:absolute;left:165px;top:2256px;display:flex;gap:4px}
.pager span{width:18px;height:18px;border:1px solid #333;font-size:9px;font-weight:700;display:flex;align-items:center;justify-content:center}
.pager span.on{background:#111;color:#fff}

.search{position:absolute;left:783px;top:1188px;width:255px;height:42px;border:1px solid var(--line);font-size:10px;color:#999;padding:14px 12px}
.side-title{position:absolute;left:783px;font-size:14px;font-weight:700;letter-spacing:.5px}

/* dark band */
.band{top:2841px;height:384px;background:var(--night);color:#fff}
.band-card{position:absolute;top:60px;width:201px}
.band-card .ph{left:0;top:0;width:201px;height:198px;position:relative}
.band-card .tag{position:absolute;left:12px;top:190px}
.band-card h4{margin-top:26px;font-size:12px;line-height:17px;font-weight:700;text-align:center}
.band-card .meta{justify-content:center;margin-top:10px}

/* popular */
.popular{top:3225px;height:609px}
.popular h2{position:absolute;left:0;width:1200px;top:52px;text-align:center;font-size:32px;font-weight:500}
.pop-item{position:absolute;width:198px}
.pop-item .ph{position:relative;width:198px;height:120px}
.pop-item .tag{margin-top:10px}
.pop-item h4{font-size:12px;line-height:17px;font-weight:700;margin:6px 0 6px}
.pop-main{position:absolute;left:393px;top:135px;width:414px;height:405px}
.pop-main .box{position:absolute;left:36px;right:36px;bottom:0;height:96px;background:#fff;text-align:center;padding-top:4px}
.pop-main h3{font-size:17px;font-weight:700;line-height:22px;margin:8px 0 0}

/* footer */
.site-footer{top:3834px;height:666px;background:var(--night);color:#fff}
.f-head{position:absolute;top:78px;font-size:13px;font-weight:700;letter-spacing:.3px}
.site-footer .mini h4{color:#fff}
.gallery{position:absolute;left:474px;top:126px;width:240px;display:grid;grid-template-columns:repeat(3,78px);grid-auto-rows:88px;gap:3px}
.gallery .ph{position:relative}
.copy{position:absolute;left:0;width:1200px;top:556px;text-align:center;font-size:9px;color:#bdbdbd;letter-spacing:.5px}
</style>
</head>
<body>

<header class="site-header">
  <div class="ph backdrop t-canyon" role="img" aria-label="Red canyon rock walls"></div>
  <div class="abs top-icons"><i></i><i></i><i></i><i></i><i></i></div>
  <div class="abs logo">BrightWanderDoc</div>
  <div class="abs tools">
    <svg width="18" height="18" viewBox="0 0 18 18"><circle cx="7.5" cy="7.5" r="5.5" fill="none" stroke="#fff" stroke-width="2.2"/><line x1="11.5" y1="11.5" x2="16" y2="16" stroke="#fff" stroke-width="2.5"/></svg>
    <svg width="18" height="16" viewBox="0 0 18 16"><rect y="1" width="18" height="2.5" fill="#fff"/><rect y="7" width="18" height="2.5" fill="#fff"/><rect y="13" width="18" height="2.5" fill="#fff"/></svg>
  </div>
  <nav class="abs nav"><span>Home</span><span>Features</span><span>Travel</span><span>Lifestyle</span><span>Medicine</span><span>Shop</span><span>Contact Us</span></nav>

  <article class="abs hero-card on-dark" style="left:165px">
    <div class="ph t-ruins" role="img" aria-label="Ancient stone library facade"></div>
    <div class="cap"><span class="tag">Lifestyle</span><h3>Lorem Ipsum is simply dummy Text of the printing</h3><p class="meta"><span class="c">2 Comments</span><span class="d">July 5, 2016</span></p></div>
  </article>
  <article class="abs hero-card on-dark" style="left:459px">
    <div class="ph t-dock" role="img" aria-label="Traveller sitting on a wooden pier by the sea"></div>
    <div class="cap"><span class="tag">Travel</span><h3>Lorem Ipsum is simply dummy Text of the printing</h3><p class="meta"><span class="c">2 Comments</span><span class="d">July 5, 2016</span></p></div>
  </article>
  <article class="abs hero-card on-dark" style="left:753px">
    <div class="ph t-beach" role="img" aria-label="Tropical beach with palm trees"></div>
    <div class="cap"><span class="tag">Lifestyle</span><h3>Lorem Ipsum is simply dummy Text of the printing</h3><p class="meta"><span class="c">2 Comments</span><span class="d">July 5, 2016</span></p></div>
  </article>
</header>

<section class="content" style="top:504px;height:2337px">
  <article class="card on-dark" style="left:165px;top:39px;width:570px;height:300px">
    <div class="ph t-lagoon" role="img" aria-label="Green lagoon between limestone cliffs"></div>
    <div class="cap"><span class="tag">Lifestyle</span><h3>Lorem Ipsum is simply dummy Text of the printing</h3><p class="meta"><span class="c">2 Comments</span><span class="d">July 9, 2016</span></p></div>
  </article>
  <div class="dots" style="top:357px"><i class="on"></i><i></i><i></i><i></i></div>

  <div class="side">
    <div class="ph t-spiral" role="img" aria-label="Aerial view of a spiral terraced landscape" style="left:783px;top:39px;width:255px;height:237px"></div>
    <article class="mini" style="left:783px;top:300px"><div class="ph t-temple" role="img" aria-label="Temple at sunset"></div><h4>Lorem Ipsum is simply dummy Text of the printing</h4><p class="meta"><span class="c">2 Comments</span><span class="d">July 9, 2016</span></p></article>
    <article class="mini" style="left:783px;top:396px"><div class="ph t-skyline" role="img" aria-label="City skyline"></div><h4>Lorem Ipsum is simply dummy Text of the printing</h4><p class="meta"><span class="c">2 Comments</span><span class="d">July 9, 2016</span></p></article>
    <article class="mini" style="left:783px;top:492px"><div class="ph t-city" role="img" aria-label="Harbour at night"></div><h4>Lorem Ipsum is simply dummy Text of the printing</h4><p class="meta"><span class="c">2 Comments</span><span class="d">July 9, 2016</span></p></article>
    <article class="mini" style="left:783px;top:588px"><div class="ph t-palace" role="img" aria-label="Palace with domes"></div><h4>Lorem Ipsum is simply dummy Text of the printing</h4><p class="meta"><span class="c">2 Comments</span><span class="d">July 9, 2016</span></p></article>

    <div class="social s-friend" style="top:717px">Friendbook</div>
    <div class="social s-chirp" style="top:777px">Chirper</div>
    <div class="social s-link" style="top:837px">LinkUp</div>
    <div class="social s-view" style="top:897px">ViewTube</div>
  </div>

  <article class="card on-dark" style="left:165px;top:417px;width:270px;height:240px">
    <div class="ph t-warm" role="img" aria-label="Woman posing outdoors in warm light"></div>
    <div class="cap"><span class="tag">Lifestyle</span><h3>Lorem Ipsum is simply dummy Text of the printing</h3><p class="meta"><span class="c">2 Comments</span><span class="d">July 9, 2016</span></p></div>
  </article>
  <article class="card on-dark" style="left:465px;top:417px;width:270px;height:240px">
    <div class="ph t-road" role="img" aria-label="Red car on an open road"></div>
    <div class="cap"><span class="tag">Travel</span><h3>Lorem Ipsum is simply dummy Text of the printing</h3><p class="meta"><span class="c">2 Comments</span><span class="d">July 9, 2016</span></p></div>
  </article>

  <article class="mini" style="left:165px;top:690px"><div class="ph t-temple" role="img" aria-label="Temple landscape"></div><h4>Lorem Ipsum is simply dummy Text of the printing</h4><p class="meta"><span class="c">2 Comments</span><span class="d">July 9, 2016</span></p></article>
  <article class="mini" style="left:465px;top:690px"><div class="ph t-canal" role="img" aria-label="Canal houses"></div><h4>Lorem Ipsum is simply dummy Text of the printing</h4><p class="meta"><span class="c">2 Comments</span><span class="d">July 9, 2016</span></p></article>
  <article class="mini" style="left:165px;top:783px"><div class="ph t-city" role="img" aria-label="City lights"></div><h4>Lorem Ipsum is simply dummy Text of the printing</h4><p class="meta"><span class="c">2 Comments</span><span class="d">July 9, 2016</span></p></article>
  <article class="mini" style="left:465px;top:783px"><div class="ph t-skyline" role="img" aria-label="Desert city"></div><h4>Lorem Ipsum is simply dummy Text of the printing</h4><p class="meta"><span class="c">2 Comments</span><span class="d">July 9, 2016</span></p></article>
  <article class="mini" style="left:165px;top:876px"><div class="ph t-palace" role="img" aria-label="Historic palace"></div><h4>Lorem Ipsum is simply dummy Text of the printing</h4><p class="meta"><span class="c">2 Comments</span><span class="d">July 9, 2016</span></p></article>
  <article class="mini" style="left:465px;top:876px"><div class="ph t-tiger" role="img" aria-label="Wild cat in the grass"></div><h4>Lorem Ipsum is simply dummy Text of the printing</h4><p class="meta"><span class="c">2 Comments</span><span class="d">July 9, 2016</span></p></article>

  <div class="ph t-rock" role="img" aria-label="Advertising banner with red rock scenery" style="left:234px;top:1020px;width:732px;height:90px"></div>

  <article class="lead">
    <div class="ph t-city" role="img" aria-label="Waterfront city skyline at dusk" style="left:165px;top:1176px;width:570px;height:300px"></div>
    <span class="tag abs" style="left:165px;top:1506px">Lifestyle</span>
    <h2 class="abs" style="left:165px;top:1524px;width:570px">Lorem Ipsum is simply dummy Text of the printing</h2>
    <p class="meta abs" style="left:165px;top:1558px"><span class="c">2 Comments</span><span class="d">July 9, 2016</span></p>
    <p class="excerpt abs" style="left:165px;top:1580px;width:570px">Morbi iaculis vehicula enim. Proin enim lorem, faucibus id tempor id, dictum quis nisl. Nam nunc enim, consectetur vitae justo non, pharetra mattis purus. Nullam scelerisque nisl sem, sed vehicula tortor finibus quis. Donec vel tempor elit, vitae facilisis neque. Integer vitae justo non pharetra mattis, blandit tellus lacus eget ultrices. Duis id lorem tortor, sed ornare lectus. Nullam finibus metus vel sem, aliquet elementum purus iaculis. Sed feugiat cursus tellus, vel pretium metus tempus a. Aenean non arcu.</p>
  </article>

  <article class="post-row" style="top:1722px"><div class="ph t-mount" role="img" aria-label="Hiker on a rocky summit"></div><div class="body"><span class="tag">Travel</span><h4>Lorem Ipsum is simply dummy Text of the printing</h4><p class="meta"><span class="c">2 Comments</span><span class="d">July 9, 2016</span></p><p class="excerpt" style="margin-top:8px">Morbi iaculis vehicula enim. Proin enim lorem, faucibus id tempor id, dictum quis nisl. Nam nunc enim, consectetur vitae justo non, pharetra mattis purus.</p></div></article>
  <article class="post-row" style="top:1887px"><div class="ph t-peaks" role="img" aria-label="Jagged mountain peaks above a meadow"></div><div class="body"><span class="tag">Lifestyle</span><h4>Lorem Ipsum is simply dummy Text of the printing</h4><p class="meta"><span class="c">2 Comments</span><span class="d">July 9, 2016</span></p><p class="excerpt" style="margin-top:8px">Morbi iaculis vehicula enim. Proin enim lorem, faucibus id tempor id, dictum quis nisl. Nam nunc enim, consectetur vitae justo non, pharetra mattis purus.</p></div></article>
  <article class="post-row" style="top:2052px"><div class="ph t-desert" role="img" aria-label="Motorbike on a desert road"></div><div class="body"><span class="tag">Lifestyle</span><h4>Lorem Ipsum is simply dummy Text of the printing</h4><p class="meta"><span class="c">2 Comments</span><span class="d">July 9, 2016</span></p><p class="excerpt" style="margin-top:8px">Morbi iaculis vehicula enim. Proin enim lorem, faucibus id tempor id, dictum quis nisl. Nam nunc enim, consectetur vitae justo non, pharetra mattis purus.</p></div></article>

  <div class="pager"><span class="on">1</span><span>2</span><span>3</span><span>4</span><span>5</span><span>6</span></div>

  <div class="side">
    <div class="search">Search
      <svg class="abs" style="right:12px;top:13px" width="14" height="14" viewBox="0 0 18 18"><circle cx="7.5" cy="7.5" r="5.5" fill="none" stroke="#111" stroke-width="2.4"/><line x1="11.5" y1="11.5" x2="16" y2="16" stroke="#111" stroke-width="2.6"/></svg>
    </div>
    <h3 class="side-title" style="top:1287px;left:828px">MOST POPULAR</h3>
    <article class="mini" style="left:783px;top:1356px"><div class="ph t-canal" role="img" aria-label="Riverside town"></div><h4>Lorem Ipsum is simply dummy Text of the printing</h4><p class="meta"><span class="c">2 Comments</span><span class="d">July 9, 2016</span></p></article>
    <article class="mini" style="left:783px;top:1452px"><div class="ph t-temple" role="img" aria-label="Temple grounds"></div><h4>Lorem Ipsum is simply dummy Text of the printing</h4><p class="meta"><span class="c">2 Comments</span><span class="d">July 9, 2016</span></p></article>
    <article class="mini" style="left:783px;top:1548px"><div class="ph t-city" role="img" aria-label="Evening harbour"></div><h4>Lorem Ipsum is simply dummy Text of the printing</h4><p class="meta"><span class="c">2 Comments</span><span class="d">July 9, 2016</span></p></article>
    <article class="mini" style="left:783px;top:1644px"><div class="ph t-palace" role="img" aria-label="Domed monument"></div><h4>Lorem Ipsum is simply dummy Text of the printing</h4><p class="meta"><span class="c">2 Comments</span><span class="d">July 9, 2016</span></p></article>
    <article class="card on-dark" style="left:783px;top:1752px;width:255px;height:234px">
      <div class="ph t-skyline" role="img" aria-label="Hillside city view"></div>
      <div class="cap"><h3 style="font-size:12px;line-height:17px">Lorem Ipsum is simply dummy Text of the printing</h3><p class="meta"><span class="c">2 Comments</span><span class="d">July 9, 2016</span></p></div>
    </article>
    <div class="ph t-spiral" role="img" aria-label="Aerial view of spiral terraces" style="left:783px;top:2031px;width:255px;height:234px"></div>
  </div>
</section>

<section class="band">
  <article class="band-card" style="left:165px"><div class="ph t-peaks" role="img" aria-label="Motorbike on a mountain road"></div><span class="tag">Lifestyle</span><h4>Lorem Ipsum is simply dummy Text of the printing</h4><p class="meta"><span class="c">2 Comments</span><span class="d">July 9, 2016</span></p></article>
  <article class="band-card" style="left:390px"><div class="ph t-ship" role="img" aria-label="Tall sailing ship"></div><span class="tag">Lifestyle</span><h4>Lorem Ipsum is simply dummy Text of the printing</h4><p class="meta"><span class="c">2 Comments</span><span class="d">July 9, 2016</span></p></article>
  <article class="band-card" style="left:615px"><div class="ph t-tower" role="img" aria-label="Clock tower in autumn"></div><span class="tag">Travel</span><h4>Lorem Ipsum is simply dummy Text of the printing</h4><p class="meta"><span class="c">2 Comments</span><span class="d">July 9, 2016</span></p></article>
  <article class="band-card" style="left:840px"><div class="ph t-pagoda" role="img" aria-label="Pagoda at sunrise"></div><span class="tag">Lifestyle</span><h4>Lorem Ipsum is simply dummy Text of the printing</h4><p class="meta"><span class="c">2 Comments</span><span class="d">July 9, 2016</span></p></article>
</section>

<section class="popular">
  <h2>Most Popular Posts</h2>
  <article class="pop-item" style="left:165px;top:135px"><div class="ph t-tiger" role="img" aria-label="White tiger resting"></div><span class="tag">Lifestyle</span><h4>Lorem Ipsum is simply dummy Text of the printing</h4><p class="meta"><span class="c">2 Comments</span><span class="d">July 9, 2016</span></p></article>
  <article class="pop-item" style="left:165px;top:363px"><div class="ph t-wall" role="img" aria-label="Ancient wall over green hills"></div><span class="tag">Lifestyle</span><h4>Lorem Ipsum is simply dummy Text of the printing</h4><p class="meta"><span class="c">2 Comments</span><span class="d">July 9, 2016</span></p></article>
  <article class="pop-main">
    <div class="ph t-palm" role="img" aria-label="Palm trees over a turquoise beach" style="inset:0"></div>
    <div class="box"><span class="tag">Lifestyle</span><h3>Lorem Ipsum is simply dummy<br>Text of the printing</h3></div>
  </article>
  <article class="pop-item" style="left:840px;top:135px"><div class="ph t-canal" role="img" aria-label="Colourful canal houses"></div><span class="tag">Lifestyle</span><h4>Lorem Ipsum is simply dummy Text of the printing</h4><p class="meta"><span class="c">2 Comments</span><span class="d">July 9, 2016</span></p></article>
  <article class="pop-item" style="left:840px;top:363px"><div class="ph t-palace" role="img" aria-label="White marble mausoleum"></div><span class="tag">Lifestyle</span><h4>Lorem Ipsum is simply dummy Text of the printing</h4><p class="meta"><span class="c">2 Comments</span><span class="d">July 9, 2016</span></p></article>
</section>

<footer class="site-footer on-dark">
  <h3 class="f-head" style="left:159px">MOST POPULAR</h3>
  <h3 class="f-head" style="left:474px">GALLERY</h3>
  <h3 class="f-head" style="left:774px">LATEST</h3>

  <article class="mini" style="left:159px;top:147px"><div class="ph t-canal" role="img" aria-label="Town by the river"></div><h4>Lorem Ipsum is simply dummy Text of the printing</h4><p class="meta"><span class="c">2 Comments</span><span class="d">July 9, 2016</span></p></article>
  <article class="mini" style="left:159px;top:240px"><div class="ph t-temple" role="img" aria-label="Temple"></div><h4>Lorem Ipsum is simply dummy Text of the printing</h4><p class="meta"><span class="c">2 Comments</span><span class="d">July 9, 2016</span></p></article>
  <article class="mini" style="left:159px;top:333px"><div class="ph t-city" role="img" aria-label="Harbour lights"></div><h4>Lorem Ipsum is simply dummy Text of the printing</h4><p class="meta"><span class="c">2 Comments</span><span class="d">July 9, 2016</span></p></article>
  <article class="mini" style="left:159px;top:426px"><div class="ph t-palace" role="img" aria-label="Monument"></div><h4>Lorem Ipsum is simply dummy Text of the printing</h4><p class="meta"><span class="c">2 Comments</span><span class="d">July 9, 2016</span></p></article>

  <div class="gallery">
    <div class="ph t-tiger" role="img" aria-label="Tiger"></div>
    <div class="ph t-ship" role="img" aria-label="Tall tower by the sea"></div>
    <div class="ph t-city" role="img" aria-label="Night skyline"></div>
    <div class="ph t-pagoda" role="img" aria-label="Pagoda"></div>
    <div class="ph t-skyline" role="img" aria-label="City view"></div>
    <div class="ph t-tower" role="img" aria-label="Clock tower"></div>
    <div class="ph t-palm" role="img" aria-label="Beach"></div>
    <div class="ph t-ruins" role="img" aria-label="Ruins"></div>
    <div class="ph t-wall" role="img" aria-label="Green hills"></div>
    <div class="ph t-peaks" role="img" aria-label="Mountain road"></div>
    <div class="ph t-palace" role="img" aria-label="Palace"></div>
    <div class="ph t-desert" role="img" aria-label="Desert road"></div>
  </div>

  <article class="mini" style="left:774px;top:147px"><div class="ph t-temple" role="img" aria-label="Temple"></div><h4>Lorem Ipsum is simply dummy Text of the printing</h4><p class="meta"><span class="c">2 Comments</span><span class="d">July 9, 2016</span></p></article>
  <article class="mini" style="left:774px;top:240px"><div class="ph t-skyline" role="img" aria-label="City view"></div><h4>Lorem Ipsum is simply dummy Text of the printing</h4><p class="meta"><span class="c">2 Comments</span><span class="d">July 9, 2016</span></p></article>
  <article class="mini" style="left:774px;top:333px"><div class="ph t-canal" role="img" aria-label="Canal"></div><h4>Lorem Ipsum is simply dummy Text of the printing</h4><p class="meta"><span class="c">2 Comments</span><span class="d">July 9, 2016</span></p></article>
  <article class="mini" style="left:774px;top:426px"><div class="ph t-city" role="img" aria-label="Harbour"></div><h4>Lorem Ipsum is simply dummy Text of the printing</h4><p class="meta"><span class="c">2 Comments</span><span class="d">July 9, 2016</span></p></article>

  <p class="copy">© 2016 ALL RIGHT RESERVED. BRIGHTWANDERDOC</p>
</footer>

</body>
</html>
```